The task involves the design and creation of a wordpress website for plainpacts.co.
Plainpacts.co is a website through which people can purchase template legal contracts.The website is focused on Australian users although in the future we may target users in other countries.
*************************************************
We will offer 3 bundles of products (a small business, medium business and a large business bundle) as follows:
(a) a Starter package ($199);
(b) a Pro (professional) package ($499);
(c) an Enterprise package ($1,500).
Each bundle contains a number of legal templates. The Pro package includes all of the legal templates in the Starter package. The Enterprise version contains all the legal templates in the Starter and Pro package.
The starter bundle will include the following legal documents:
+Website terms and conditions
+Confidentiality agreement
+Services agreement
+Purchase order terms and conditions
+Variation agreement
+Independent contractor agreement
+Term sheet
The Pro bundle includes:
+ all of the documents contained in the Starter package plus
+ Request for tender
+ Consultancy agreement
+ Contract labour agreement
+ Sponsorship agreement
The Enterprise package includes:
+All of the documents in our Pro package plus
+Freight Services agreement
+IT Services agreement
+Website design and hosting agreement
+Teaming agreement
+Long form services agreement
+Distribution agreement
+Content supply agreement
****************************************************
We like the simplicity and layout of the following websites:
http://leavewatcher.com/
https://www.trymeadow.com/
http://www.helpquarry.com/
http://www.nodlegal.com/
http://usebrindle.com/
We like the way on the leavewatcher.com page when you click on the pricing tab and other tabs of the navigation bar you are taken lower down on the homepage to the content. We like the static header on leavewatcher and Helpquarry. We also like the use of big headings, images and symbols to convey meaning as well as having the webpage broken into sections.
We will want an email sign up capability and will need to integrate an email collection capability with postwren or similar.
We like the way it is referred to on the https://www.harbordocs.com/ website where it says:
"Your first document is free" and them there is an email sign up box.
We imagine having a similar features at a couple of places on the site with a call to action.
We also imagine including some sort of website abandonment application similar to http://leavewatcher.com/ or http://pagetrellis.com/. We would also like a countdown clock linked to a discount off the price of the bundles. Please provide a recommendation and ensure that this can easily be integrated.
We will need an e-commence capability so that we can sell our products.
******************************************
Our value proposition is as follows:
1. Lower your legal costs by using our template documents as a starting point
Why pay a lawyer to create a document from scratch when you can you our template agreements as the starting point.
2. Variety of bundles to chose from
We offer you the opportunity to purchase the bundle of documents that are just right for you – small business, medium business and large business options.
3.Customise agreements yourself or have your lawyer customise them for you.
Our contracts are drafted in plain English and you can provide them to your lawyer and ask them to customise them for you.
4. Reviewed by top lawyers - customised for Australia
All of our legal documents have been reviewed by a lawyer with experience working at a top international law firm.
***************************************************
The benefits of the service are:
* Documents reviewed by Australian lawyer with experience at top tier Australian law firm.
* Cost effective approach to risk management
* Electronic delivery
* Use templates as often as you like for your internal business purposes
* Free explanation of each template agreement
* Sensible approach to legal drafting to minimise contract negotiation time
*****************************************************
We will need to include the following across the bottom of each webpage.
"Copyright 2014 PlainPacts. All rights reserved. PlainPacts provides information only. PlainPacts is not a "lawyer referral service" and does not provide legal advice or participate in any legal representation. PlainPacts is not a law firm or a substitute for a qualified lawyer or law firm. For legal advice, please contact a lawyer. Use of PlainPacts.co is subject to our Terms and Conditions."
The reference to Terms and Conditions will be a link to the Terms and Conditions.
*********************************************************
The Contact Us section should be a simple webform. We will not include any telephone or physical address at this stage.
For the About Us section
We can include the following:
PlainPacts was conceived and nurtured in Melbourne, the world's most liveable city by an experienced lawyer who loves the idea of making legal contracting affordable for small and medium size businesses. We have friends in other cities who help make PlainPacts possible.
************************************************************
We expect the website created to be user friendly, able to be updated easily, optimised for search engines and to be built on wordpress. The website should be able to integrate with third party applications (eg analytic software, email marketing tools etc). Please include recommendations for third party software for integration. We have installed Wordpress 3.9.
Target Market(s)
Small to medium business owners.

```html
<!DOCTYPE html>
<html lang="en">
<head>
<meta charset="utf-8">
<title>Products – PlainPacts.co</title>
<link href="https://fonts.googleapis.com/css2?family=Domine:wght@400;700&family=Arimo&display=swap" rel="stylesheet">
<style>
:root{
  --mint:#3ff8bd;
  --mint-soft:#4ff5bc;
  --mint-deep:#22c493;
  --page:#f6f9fb;
  --white:#ffffff;
  --ink:#222222;
  --muted:#555555;
  --price:#6cc24a;
  --rule:#dfe3e6;
  --slider:#8a3fd1;
}
*{box-sizing:border-box;margin:0;padding:0}
html,body{width:1119px;height:1200px;overflow:hidden}
body{background:var(--page);font-family:'Domine',Georgia,serif;color:var(--ink);position:relative;font-size:10px}
a{color:inherit;text-decoration:none}

.cart-bar{position:absolute;left:0;top:0;width:1105px;height:33px;background:var(--mint);color:var(--white);font-size:11px}
.cart-bar .cart{position:absolute;left:164px;top:9px;display:flex;align-items:center;gap:5px}
.cart-bar .account-links{position:absolute;right:175px;top:10px;display:flex;gap:15px}

.site-header{position:absolute;left:0;top:33px;width:1105px;height:60px;background:var(--white);border-bottom:1px solid var(--rule)}
.brand{position:absolute;left:164px;top:18px;display:flex;align-items:center;gap:6px;font-size:20px;color:var(--mint-deep);font-weight:400}
.brand .mark{width:12px;height:12px;background:var(--mint)}
.main-nav{position:absolute;right:168px;top:21px;display:flex;gap:24px;font-size:11px}
.main-nav .current{color:var(--mint-deep)}

.shop{position:absolute;left:164px;top:150px;width:516px}
.shop h1{font-size:19px;font-weight:400;position:absolute;top:22px;left:0}
.sort{position:absolute;left:342px;top:15px;width:174px;height:25px;border:1px solid var(--rule);background:var(--white);font-family:'Arimo',Arial,sans-serif;font-size:9px;color:var(--muted);padding:7px 11px}
.sort svg{position:absolute;right:14px;top:7px}
.shop .divider{position:absolute;top:64px;left:0;width:516px;border-top:1px dashed var(--rule)}
.result-count{position:absolute;top:79px;left:0;font-size:11px}

.card{position:absolute;width:159px;background:var(--white);box-shadow:0 1px 3px rgba(0,0,0,.18);padding:8px 7px}
.card .tile{height:108px;background:var(--mint);color:var(--white);font-family:'Arimo',Arial,sans-serif;font-size:27px;line-height:1.17;display:flex;align-items:center;justify-content:center;text-align:center}
.card .price{color:var(--price);font-size:12px;margin-top:16px}
.card h2{font-size:12px;font-weight:400;margin-top:6px}
.card p{font-size:9.4px;line-height:16.4px;margin-top:4px;color:var(--ink)}
.card p .link{color:#1e3a8a}

.sidebar{position:absolute;left:735px;top:136px;width:207px}
.sidebar .label{font-size:11px}
.search-row{display:flex;gap:6px;margin-top:4px}
.search-row .field{width:143px;height:17px;border:1px solid #bfc5c9;background:var(--white);font-family:'Arimo',Arial,sans-serif;font-size:10px;color:#999;padding:2px 3px}
.btn{height:17px;border:1px solid #a9adb1;background:linear-gradient(#fdfdfd,#e4e6e8);font-family:'Arimo',Arial,sans-serif;font-size:10px;padding:2px 6px;border-radius:2px}
.sidebar h3{font-size:14px;font-weight:700;margin-top:15px;padding-bottom:10px;border-bottom:1px solid var(--rule)}
.range{margin-top:8px}
.filter-row{display:flex;justify-content:space-between;align-items:center;margin-top:6px}
.filter-row .btn{height:20px;padding:3px 8px;font-family:'Domine',serif}
.filter-row .amount{font-size:9.5px;color:var(--muted)}

.site-footer{position:absolute;left:0;top:916px;width:1105px;height:184px;background:var(--mint-soft);border-top:1px solid var(--mint-deep)}
.footer-col{position:absolute;top:22px;color:var(--white)}
.footer-col h4{font-size:12px;font-weight:400;color:#169c72;padding-bottom:3px;border-bottom:1px dotted #169c72;display:inline-block}
.footer-search{display:flex;margin-top:10px}
.footer-search .field{width:135px;height:27px;background:var(--white);border:1px solid #cde;font-family:'Arimo',Arial,sans-serif;font-size:10px;color:#555;padding:7px 6px}
.footer-search .go{width:27px;height:27px;background:var(--mint);display:flex;align-items:center;justify-content:center}
.trending a{display:block;font-size:8px;line-height:17px;margin-top:8px;width:140px}
.about-text{font-size:11px;line-height:17px;margin-top:8px;width:172px}
.payment{position:absolute;left:760px;top:20px;width:120px;text-align:center}
.payment .seal{width:52px;height:52px;border-radius:50%;background:#f1d43a;margin:0 auto}
.payment .name{font-size:18px;color:var(--white);font-weight:700;margin-top:4px}
.cards{display:flex;gap:3px;justify-content:center;margin-top:4px}
.cards span{width:23px;height:14px;background:var(--white);border:1px solid #cfd}

.legal-bar{position:absolute;left:0;top:1100px;width:1105px;height:100px;background:var(--mint-deep);border-top:1px dashed #169c72;color:var(--white)}
.social{position:absolute;left:164px;top:15px;display:flex;gap:11px}
.social span{width:19px;height:19px;border-radius:50%;background:var(--white)}
.legal{position:absolute;right:163px;top:17px;width:560px;text-align:right;font-size:11px;line-height:17.2px}
.legal a{color:var(--mint)}
.scroll-track{position:absolute;right:0;top:0;width:14px;height:1200px;background:#f1f1f1}
.scroll-track .thumb{position:absolute;left:3px;top:14px;width:9px;height:316px;background:#c1c1c1}
</style>
</head>
<body>

<div class="cart-bar">
  <div class="cart">
    <svg width="16" height="12" viewBox="0 0 16 12" fill="none" stroke="#fff" stroke-width="1.3"><path d="M1 1h2l2 7h8l2-5H4"/><circle cx="6" cy="10.5" r="1"/><circle cx="12" cy="10.5" r="1"/></svg>
    <span>0 items - ( $0 in total )</span>
  </div>
  <nav class="account-links"><a href="#">Register</a><a href="#">Login</a></nav>
</div>

<header class="site-header">
  <a class="brand" href="#"><span class="mark"></span>PlainPacts.co</a>
  <nav class="main-nav">
    <a href="#">Home</a><a href="#">About</a><a href="#" class="current">Products</a><a href="#">My Account</a><a href="#">Contact</a>
  </nav>
</header>

<main class="shop">
  <h1>Products</h1>
  <div class="sort">Sort by price: low to high
    <svg width="8" height="11" viewBox="0 0 8 11" fill="#999"><path d="M4 0l4 4H0zM4 11L0 7h8z"/></svg>
  </div>
  <div class="divider"></div>
  <p class="result-count">Showing all 4 results</p>
</main>

<article class="card" style="left:164px;top:256px;height:250px">
  <div class="tile">XYZ<br>Document</div>
  <div class="price">Free</div>
  <h2>Free Doucment</h2>
  <p>To demonstrate our capacity to develop and deliver quality legal documentation, please accept this document …</p>
</article>
<article class="card" style="left:342px;top:256px;height:250px">
  <div class="tile">Standard<br>Package</div>
  <div class="price">$199</div>
  <h2>Standard Package</h2>
  <p>Our small business bundle includes everything you need to establish yourself! Example text will continue …</p>
</article>
<article class="card" style="left:520px;top:256px;height:250px">
  <div class="tile">Pro<br>Package</div>
  <div class="price">$499</div>
  <h2>Pro Package</h2>
  <p>Our Professional Package is targeted towards medium business’ and includes everything you need as a …</p>
</article>
<article class="card" style="left:164px;top:527px;height:300px">
  <div class="tile">Enterprise<br>Package</div>
  <div class="price">$1,500</div>
  <h2>Enterprise Package</h2>
  <p>Our<br>Enterprise Package provides a <span class="link">holistic</span> solution for<br>large business!<br>All of the documents contained in the Starter and<br>…</p>
</article>

<aside class="sidebar">
  <div class="label">Search for:</div>
  <div class="search-row"><div class="field">Search for packages</div><div class="btn">Search</div></div>
  <h3>Filter by price</h3>
  <svg class="range" width="207" height="14" viewBox="0 0 207 14"><rect x="5" y="5" width="197" height="4" rx="2" fill="#8a3fd1"/><circle cx="6" cy="7" r="5.5" fill="#b08ce0" stroke="#6a2aa8"/><circle cx="201" cy="7" r="5.5" fill="#b08ce0" stroke="#6a2aa8"/></svg>
  <div class="filter-row"><div class="btn">Filter</div><div class="amount">Price: $0 — $1500</div></div>
</aside>

<footer class="site-footer">
  <div class="footer-col" style="left:164px">
    <h4>Search PlainPacts.co</h4>
    <div class="footer-search"><div class="field">Search</div><div class="go">
      <svg width="11" height="11" viewBox="0 0 11 11" fill="none" stroke="#fff" stroke-width="1.6"><circle cx="4.5" cy="4.5" r="3.3"/><path d="M7 7l3.3 3.3"/></svg></div></div>
  </div>
  <div class="footer-col trending" style="left:368px">
    <h4>Trending</h4>
    <a href="#">Enterprise instant access New Legislation</a>
  </div>
  <div class="footer-col" style="left:565px">
    <h4>About</h4>
    <p class="about-text">PlainPacts is part of the XYZ group of companies, providing cost effective legal documentation for businesses in Australia.</p>
  </div>
  <div class="payment">
    <div class="seal" role="img" aria-label="Verified payment badge"></div>
    <div class="name">Payvault</div>
    <div class="cards"><span></span><span></span><span></span><span></span><span></span></div>
  </div>
</footer>

<div class="legal-bar">
  <div class="social"><span></span><span></span><span></span><span></span></div>
  <p class="legal">Copyright 2014 PlainPacts. All rights reserved. PlainPacts provides information only. PlainPacts is not a "lawyer referral service" and does not provide legal advice or participate in any legal representation. PlainPacts is not a law firm or a substitute for a qualified lawyer or law firm. For legal advice, please contact a lawyer. Use of PlainPacts.co is subject to our <a href="#">Terms and Conditions</a></p>
</div>

<div class="scroll-track"><div class="thumb"></div></div>

</body>
</html>
```